Varolta Business Card

I am looking for a business card design for a start-up company called Varolta Group. This is a management consultancy focused on sales, marketing, sales management, product management and AGILE software development. Our primary customers are $1M to $50M in revenue.

Varolta is the Italian word for "slope."

The path from $0 to $50M has many different growth stages associated with it. Each one having a significant slope to the next plateau. Our expertise helps our customers ascend each of those slopes. We bring experience, successful track-records in growing companies, best practices and a dive-in and roll-up your sleeves mentality. We are not sitting at base camp shouting instructions, we are right there with you, on the climb.

Industry/Entity Type

Business

```html
<!DOCTYPE html>
<html lang="en">
<head>
<meta charset="utf-8">
<title>Varolta Business Card</title>
<link rel="stylesheet" href="https://fonts.googleapis.com/css2?family=Roboto:wght@300;400&display=swap">
<style>
  :root {
    --page: #e6e4e1;
    --blue-light: #1d7fc0;
    --blue-dark: #0b4a86;
    --green: #6aa532;
    --card-white: #f1f1f1;
    --ink: #5b6670;
    --label: #2a8ad0;
  }
  * { margin: 0; padding: 0; box-sizing: border-box; }
  html, body { width: 1200px; height: 900px; overflow: hidden; }
  body {
    background: var(--page);
    font-family: "Roboto", Arial, sans-serif;
    font-weight: 300;
    position: relative;
  }
  .card {
    position: absolute;
    left: 320px;
    width: 560px;
    height: 320px;
    border-radius: 3px;
    overflow: hidden;
    box-shadow: 0 6px 18px rgba(0,0,0,0.18);
  }
  .card-front {
    top: 100px;
    background: radial-gradient(circle at 30% 70%, var(--blue-light), var(--blue-dark) 85%);
    color: #fff;
  }
  .card-back { top: 470px; background: var(--card-white); color: var(--ink); }

  .brand { display: flex; align-items: center; gap: 14px; }
  .brand-dot { border-radius: 50%; flex: none; }
  .brand-name { font-weight: 300; line-height: 1; letter-spacing: -1px; }

  .card-front .brand { position: absolute; left: 120px; top: 92px; }
  .card-front .brand-dot { width: 70px; height: 70px; background: #fff; opacity: .9; }
  .card-front .brand-name { font-size: 76px; color: #fff; }
  .card-front .web { position: absolute; right: 120px; top: 212px; font-size: 15px; letter-spacing: 1px; }

  .card-back .brand { position: absolute; left: 40px; top: 40px; }
  .card-back .brand-dot { width: 62px; height: 62px; background: var(--blue-light); }
  .card-back .brand-name { font-size: 70px; color: var(--ink); }
  .person { position: absolute; left: 116px; top: 128px; display: flex; align-items: baseline; gap: 12px; }
  .person-name { font-size: 19px; font-weight: 400; letter-spacing: .5px; }
  .person-title { font-size: 12px; }
  .contact { position: absolute; left: 116px; top: 162px; font-size: 13px; line-height: 17px; }
  .contact-row { display: flex; }
  .contact-label { width: 58px; color: var(--label); }
  .contact-web { color: var(--label); font-size: 14px; margin-top: 2px; }
  .card-band { position: absolute; left: 0; bottom: 0; }
</style>
</head>
<body>
  <section class="card card-front" aria-label="Card front">
    <div class="brand">
      <span class="brand-dot"></span>
      <span class="brand-name">Varolta</span>
    </div>
    <p class="web">www.varolta.com</p>
  </section>

  <section class="card card-back" aria-label="Card back">
    <div class="brand">
      <span class="brand-dot"></span>
      <span class="brand-name">Varolta</span>
    </div>
    <div class="person">
      <span class="person-name">DANIEL MARSH</span>
      <span class="person-title">Product Marketing Manager</span>
    </div>
    <div class="contact">
      <div class="contact-row"><span class="contact-label">phone</span><span>555.010.1234</span></div>
      <div class="contact-row"><span class="contact-label">fax</span><span>555.010.5678</span></div>
      <div class="contact-row"><span class="contact-label">email</span><span>daniel@varolta.com</span></div>
      <div class="contact-row"><span class="contact-label"></span><span>420 Harbor View Road, Suite 110, Eastfield, MA 01234</span></div>
      <div class="contact-row"><span class="contact-label"></span><span class="contact-web">www.varolta.com</span></div>
    </div>
    <svg class="card-band" width="560" height="60" viewBox="0 0 560 60" aria-hidden="true">
      <path d="M0 40 L210 40 Q226 40 232 28 L246 0 L246 60 L0 60 Z" fill="var(--blue-dark)"/>
      <path d="M238 60 Q246 44 262 44 L560 44 L560 60 Z" fill="var(--green)"/>
    </svg>
  </section>
</body>
</html>
```